Brookside Grocer

Hope all is well!

Wanted to make business cards for my father. His name is Faisal Qureshi and owns convenience stores. I have attached logo :)

He does not want any title just simple name and phone. An email would be nice as well.

Faisal Qureshi
Cell: 413-585-2046
Store: 413-719-4820

Brooksidegrocer512@fernpost.com

The design and style is totally up to you :) The colors we were looking for were the same as logo :)

```html
<!DOCTYPE html>
<html lang="en">
<head>
<meta charset="utf-8">
<title>Brookside Grocer – Business Card</title>
<link href="https://fonts.googleapis.com/css2?family=Montserrat:wght@400;500;700;800&display=swap" rel="stylesheet">
<style>
  :root {
    --backdrop: #9b9b9b;
    --card-white: #fafbfd;
    --brand-red: #d61f28;
    --brand-navy: #243a78;
    --ink: #1c1c1c;
  }
  * { margin: 0; padding: 0; box-sizing: border-box; }
  html, body {
    width: 1093px;
    height: 1200px;
    overflow: hidden;
    background: var(--backdrop);
    font-family: "Montserrat", sans-serif;
  }
  .card {
    position: absolute;
    left: 262px;
    width: 582px;
    height: 362px;
    border-radius: 18px;
  }
  .card-front { top: 223px; background: var(--card-white); }
  .card-back {
    top: 620px;
    background: var(--brand-red);
    display: flex;
    align-items: center;
    justify-content: center;
  }

  .wordmark {
    display: flex;
    align-items: center;
    gap: 10px;
    font-weight: 800;
    color: var(--brand-navy);
    white-space: nowrap;
  }
  .wordmark-dot {
    border-radius: 50%;
    background: var(--brand-red);
    flex: none;
  }
  .card-front .wordmark {
    position: absolute;
    left: 40px;
    top: 184px;
    font-size: 23px;
  }
  .card-front .wordmark-dot { width: 14px; height: 14px; }
  .card-back .wordmark { font-size: 40px; gap: 16px; }
  .card-back .wordmark-dot { width: 26px; height: 26px; background: #ffffff; }

  .divider {
    position: absolute;
    left: 315px;
    top: 111px;
    width: 1.5px;
    height: 173px;
    background: var(--brand-red);
  }
  .contact {
    position: absolute;
    left: 336px;
    top: 111px;
    color: var(--ink);
  }
  .contact-name {
    font-size: 21px;
    font-weight: 700;
    color: var(--brand-red);
    line-height: 1.1;
  }
  .contact-list {
    list-style: none;
    margin-top: 16px;
  }
  .contact-list li {
    display: flex;
    align-items: center;
    gap: 9px;
    font-size: 13px;
    height: 20px;
  }
  .contact-list li.email { font-size: 12px; letter-spacing: -0.2px; }
  .contact-list svg { width: 16px; height: 14px; flex: none; fill: var(--brand-red); }
  .contact-address {
    font-style: normal;
    font-size: 13px;
    line-height: 17.5px;
    margin-top: 14px;
    margin-left: 7px;
  }
</style>
</head>
<body>

<section class="card card-front">
  <div class="wordmark"><span class="wordmark-dot"></span>Brookside Grocer</div>
  <div class="divider"></div>
  <div class="contact">
    <p class="contact-name">Faisal Qureshi</p>
    <ul class="contact-list">
      <li>
        <svg viewBox="0 0 16 14" aria-hidden="true"><path d="M1 5c0-2 3-3 7-3s7 1 7 3v1h-3V4.5C11 4 9.5 3.8 8 3.8S5 4 4 4.5V6H1z"/><path d="M4 7h8l2 6H2z"/><circle cx="8" cy="9.5" r="1.6" fill="#fafbfd"/></svg>
        413-719-4820
      </li>
      <li>
        <svg viewBox="0 0 16 14" aria-hidden="true"><path d="M5 0h6a1 1 0 0 1 1 1v12a1 1 0 0 1-1 1H5a1 1 0 0 1-1-1V1a1 1 0 0 1 1-1zm.5 1.5v9h5v-9z"/><circle cx="8" cy="12" r="0.9" fill="#fafbfd"/></svg>
        413-585-2046
      </li>
      <li class="email">
        <svg viewBox="0 0 16 14" aria-hidden="true"><path d="M1 3h14v9H1z"/><path d="M1 3l7 5 7-5" fill="none" stroke="#fafbfd" stroke-width="1.2"/></svg>
        Brooksidegrocer512@fernpost.com
      </li>
      <li>
        <svg viewBox="0 0 16 14" aria-hidden="true"><circle cx="8" cy="7" r="6"/><path d="M5 3.5c1.5 0 2 1 1.5 2S4 6.5 4.5 8M10 4c-1 1 0 2 1.5 2.2M9 9.5c1 0 1.5 1 1 2.5" fill="none" stroke="#fafbfd" stroke-width="1.2"/></svg>
        www.Brooksidegrocer.com
      </li>
    </ul>
    <address class="contact-address">148 Alder Row, Suite 6<br>Fernvale, UT 84920</address>
  </div>
</section>

<section class="card card-back">
  <div class="wordmark"><span class="wordmark-dot"></span>Brookside Grocer</div>
</section>

</body>
</html>
```